We are an online mail order nursery selling live plants who needs a 1 page landing page for an upcom

We are opening a new sister site to our main site. The new site is membership based. We need a landing page for an email campaign that is both attention grabbing and simply luring the customer to click on the learn more about Membership Page : http://www.thefernguild.com/pages/membership-info
The landing page will need to have space reserved for a white board presentation. I have attached the video below. The vid will be hosted on You tube so we should be able to use the iframe / embed technique. Again our goal is to funnel the customer to http://www.thefernguild.com/pages/membership-info where they can get more details.

Target Market(s)

Home owners between the age of 35 and 65 - gardening enthusiast

Industry/Entity Type

Campaign

Number of Pages Required

1 page

Font styles to use
Sans Serif

Requirements
Must have
• space to embed white board video

```html
<!DOCTYPE html>
<html lang="en">
<head>
<meta charset="utf-8">
<title>The Fern Guild – Gold Membership</title>
<link rel="stylesheet" href="https://fonts.googleapis.com/css2?family=Baloo+2:wght@500&family=Open+Sans:ital,wght@0,400;0,700;1,600&display=swap">
<style>
  :root {
    --header-bg: #dcefd2;
    --header-bg-light: #eaf6e2;
    --brand-green: #2f7d2b;
    --title-blue: #1f4f86;
    --muted: #4a4a4a;
    --loyal-purple: #4b2a86;
    --cream: #fdfdee;
    --card-teal: #2fb5a5;
    --card-green: #4dbf7a;
    --card-text: #2b2b2b;
    --cta-dark: #0f6e62;
    --cta-light: #1f8f7e;
    --footer-teal: #9ccfc4;
    --play-green: #3b8f6b;
    --calendar-red: #ef5a45;
    --wallet-bg: #e9ecef;
    --gold: #f5b31b;
    --tag-pink: #c7176b;
    --truck-purple: #3a2c86;
    --mail-blue: #2ab7e8;
    --gift-green: #8cc63f;
    --presenter-blue: #b9d4ea;
    --leaf-soft: #cfe6c8;
  }
  * { box-sizing: border-box; margin: 0; padding: 0; }
  html, body { width: 757px; height: 1200px; overflow: hidden; background: #ffffff; }
  .stage {
    position: relative;
    width: 740px; height: 1173px;
    transform: scale(1.023);
    transform-origin: top left;
    font-family: "Open Sans", Arial, sans-serif;
  }

  /* Header */
  .header {
    position: absolute; left: 0; top: 0; width: 740px; height: 200px;
    background: linear-gradient(180deg, var(--header-bg-light), var(--header-bg));
    text-align: center;
  }
  .brand {
    position: absolute; top: 40px; left: 0; right: 0;
    display: flex; justify-content: center; align-items: center; gap: 12px;
  }
  .brand-dot { width: 44px; height: 44px; border-radius: 50%; background: var(--brand-green); }
  .brand-name {
    font-weight: 700; font-size: 34px; letter-spacing: 1px; color: var(--brand-green);
  }
  .headline {
    position: absolute; top: 110px; left: 0; right: 0;
    font-size: 25px; font-weight: 700; color: var(--title-blue); letter-spacing: .5px;
  }
  .tagline {
    position: absolute; top: 144px; left: 0; right: 0;
    font-size: 15px; color: var(--muted);
  }

  /* Video area */
  .video {
    position: absolute; left: 0; top: 200px; width: 740px; height: 348px; background: #ffffff;
  }
  .icon-circle { position: absolute; border-radius: 50%; }
  .icon-calendar { left: 138px; top: 92px; width: 116px; height: 116px; background: var(--calendar-red); }
  .icon-wallet { left: 483px; top: 92px; width: 116px; height: 116px; background: var(--wallet-bg); }
  .presenter {
    position: absolute; left: 281px; top: 10px; width: 175px; height: 175px; border-radius: 50%;
    background: var(--presenter-blue);
  }
  .play-button { position: absolute; left: 287px; top: 92px; width: 152px; height: 152px; }
  .loyal-note {
    position: absolute; left: 0; right: 0; top: 216px;
    font-family: "Baloo 2", "Open Sans", sans-serif; font-weight: 500;
    font-size: 29px; line-height: 30px; letter-spacing: -0.8px;
    color: var(--loyal-purple); text-align: center;
  }

  /* Benefits */
  .benefits {
    position: absolute; left: 0; top: 548px; width: 740px; height: 424px; background: var(--cream);
  }
  .benefit {
    position: absolute; width: 182px; height: 97px;
    border-radius: 12px; padding: 4px;
    background: linear-gradient(90deg, var(--card-teal), var(--card-green));
  }
  .benefit-inner {
    width: 100%; height: 100%; border-radius: 9px; background: var(--cream);
    display: flex; align-items: center; justify-content: center; text-align: center;
    font-style: italic; font-weight: 600; font-size: 13.5px; line-height: 18px; color: var(--card-text);
    padding: 14px 4px 0;
  }
  .benefit-icon { position: absolute; left: 50%; transform: translateX(-50%); top: -36px; }
  .b1 { left: 61px; top: 75px; } .b2 { left: 279px; top: 75px; } .b3 { left: 497px; top: 75px; }
  .b4 { left: 61px; top: 220px; } .b5 { left: 279px; top: 220px; }
  .cta-leaves {
    position: absolute; left: 485px; top: 185px; width: 205px; height: 175px; border-radius: 50%;
    background: radial-gradient(circle, var(--leaf-soft) 0 45%, rgba(207,230,200,0) 72%);
  }
  .cta {
    position: absolute; left: 493px; top: 223px; width: 184px; height: 90px;
    border-radius: 8px; text-decoration: none; color: #ffffff; text-align: center;
    background: linear-gradient(135deg, var(--cta-light), var(--cta-dark));
    display: flex; flex-direction: column; justify-content: center;
  }
  .cta-small { font-size: 17px; }
  .cta-big { font-size: 22px; font-weight: 700; }

  /* Footer */
  .footer {
    position: absolute; left: 0; top: 972px; width: 740px; height: 201px; background: var(--footer-teal);
  }
  .plant {
    position: absolute; left: 85px; top: 905px; width: 555px; height: 268px;
    background: linear-gradient(180deg, rgba(111,163,66,.55), rgba(111,163,66,.35));
  }
</style>
</head>
<body>
<main class="stage">
  <header class="header">
    <div class="brand"><span class="brand-dot"></span><span class="brand-name">THE FERN GUILD</span></div>
    <h1 class="headline">GOLD MEMBERSHIP PAYS</h1>
    <p class="tagline">Saving Money Is Equal Earning Money</p>
  </header>

  <section class="video" aria-label="Membership video">
    <div class="icon-circle icon-calendar">
      <svg width="116" height="116" viewBox="0 0 116 116" aria-hidden="true">
        <rect x="34" y="36" width="48" height="44" rx="3" fill="#fff"/>
        <rect x="34" y="36" width="48" height="10" fill="#e9e9e9"/>
        <rect x="41" y="30" width="4" height="10" fill="#fff"/><rect x="71" y="30" width="4" height="10" fill="#fff"/>
        <g fill="var(--calendar-red)">
          <rect x="42" y="52" width="6" height="5"/><rect x="52" y="52" width="6" height="5"/><rect x="62" y="52" width="6" height="5"/><rect x="72" y="52" width="6" height="5"/>
          <rect x="42" y="61" width="6" height="5"/><rect x="52" y="61" width="6" height="5"/><rect x="62" y="61" width="6" height="5"/><rect x="72" y="61" width="6" height="5"/>
          <rect x="42" y="70" width="6" height="5"/><rect x="52" y="70" width="6" height="5"/>
        </g>
      </svg>
    </div>
    <div class="presenter" role="img" aria-label="Illustration of a presenter in front of a city skyline"></div>
    <div class="icon-circle icon-wallet">
      <svg width="116" height="116" viewBox="0 0 116 116" aria-hidden="true">
        <rect x="38" y="30" width="40" height="24" rx="3" fill="#3b9b4a" transform="rotate(-10 58 42)"/>
        <rect x="28" y="44" width="58" height="40" rx="6" fill="var(--gold)"/>
        <rect x="66" y="56" width="22" height="14" rx="4" fill="#e29a0c"/>
        <circle cx="73" cy="63" r="3" fill="#fff"/>
      </svg>
    </div>
    <svg class="play-button" viewBox="0 0 152 152" aria-label="Play video" role="img">
      <circle cx="76" cy="76" r="70" fill="rgba(59,143,107,.85)" stroke="#ffffff" stroke-width="4"/>
      <circle cx="76" cy="76" r="62" fill="none" stroke="var(--play-green)" stroke-width="6"/>
      <path d="M62 50 L106 76 L62 102 Z" fill="#ffffff"/>
    </svg>
    <p class="loyal-note">As a loyal customer of<br>The Fern Nursery we have saved you money<br>down through the years now we have a new<br>way to save you even more.</p>
  </section>

  <section class="benefits">
    <div class="benefit b1">
      <svg class="benefit-icon" width="46" height="50" viewBox="0 0 46 50" aria-hidden="true">
        <path d="M15 4 L31 4 L27 14 L19 14 Z" fill="var(--gold)"/>
        <ellipse cx="23" cy="33" rx="21" ry="17" fill="var(--gold)"/>
        <text x="23" y="41" text-anchor="middle" font-family="Open Sans, sans-serif" font-weight="700" font-size="22" fill="#fff">$</text>
      </svg>
      <div class="benefit-inner">Save additional 30%<br>on top of the half<br>price sale for 1 year</div>
    </div>
    <div class="benefit b2">
      <svg class="benefit-icon" width="78" height="46" viewBox="0 0 78 46" aria-hidden="true">
        <path d="M4 16 L58 4 L74 14 L78 28 L12 42 Z" fill="var(--tag-pink)"/>
        <circle cx="64" cy="16" r="3" fill="#fff"/>
        <text x="34" y="32" text-anchor="middle" font-family="Open Sans, sans-serif" font-weight="700" font-size="15" fill="#fff" transform="rotate(-12 34 28)">50%</text>
      </svg>
      <div class="benefit-inner">Get half price shipping<br>on every order<br>no matter the size</div>
    </div>
    <div class="benefit b3">
      <svg class="benefit-icon" width="78" height="46" viewBox="0 0 78 46" aria-hidden="true">
        <rect x="2" y="2" width="48" height="32" fill="var(--truck-purple)"/>
        <path d="M52 12 L66 12 L76 24 L76 34 L52 34 Z" fill="var(--truck-purple)"/>
        <circle cx="16" cy="38" r="6" fill="var(--truck-purple)" stroke="#fff" stroke-width="2"/>
        <circle cx="62" cy="38" r="6" fill="var(--truck-purple)" stroke="#fff" stroke-width="2"/>
      </svg>
      <div class="benefit-inner">Free returns if you<br>are not 100% satisfied<br>with your plants</div>
    </div>
    <div class="benefit b4">
      <svg class="benefit-icon" width="62" height="40" viewBox="0 0 62 40" aria-hidden="true">
        <rect x="0" y="2" width="62" height="36" fill="var(--mail-blue)"/>
        <path d="M0 2 L31 24 L62 2" fill="none" stroke="#ffffff" stroke-width="2"/>
      </svg>
      <div class="benefit-inner">Invitation only<br>nursery liquidation /<br>Flash sales</div>
    </div>
    <div class="benefit b5">
      <svg class="benefit-icon" width="44" height="48" viewBox="0 0 44 48" aria-hidden="true">
        <rect x="2" y="14" width="40" height="10" fill="var(--gift-green)"/>
        <rect x="5" y="24" width="34" height="22" fill="var(--gift-green)"/>
        <rect x="19" y="14" width="6" height="32" fill="#fff"/>
        <path d="M22 14 C12 2 6 8 12 14 M22 14 C32 2 38 8 32 14" fill="none" stroke="var(--gift-green)" stroke-width="4"/>
      </svg>
      <div class="benefit-inner">Earn membership<br>reward point to<br>buy more plants</div>
    </div>
    <div class="cta-leaves" role="img" aria-label="Decorative leaf wreath around the button"></div>
    <a class="cta" href="http://www.thefernguild.com/pages/membership-info">
      <span class="cta-small">Learn More About</span>
      <span class="cta-big">Membership</span>
    </a>
  </section>

  <footer class="footer"></footer>
  <div class="plant" role="img" aria-label="Illustration of a leafy green plant in a pot"></div>
</main>
</body>
</html>
```